Visitenkarten für Psychotherapeutin
Zielgruppe
Ich war Psychologin und Coachin und bin jetzt eine approbierte Psychotherapeutin.
Aufgabenstellung
Es gibt ein Layout, an das sich angelehnt werden soll.
Die Farb- und Schriftwelt liegt vor, jedoch soll aus dem türkies ein warmer Pink-Rot-Ton werden.
Die Visitenkarte soll für die neu eröffnete Privatpraxis verwendet werden. Im Logo soll die Berufsbezeichnung Psychologische Psychotherapeutin (mit) Schwerpunkt Systemische Therapie stehen.
Neben den Kontaktdaten folgender Text:
Privatpraxis für Psychologische Psychotherapie, Schwerpunkt Systemische Therapie
Für Privatversicherte und Selbstzahlende
Termin nach Vereinbarung
Die Zeile mit der Sprechstunde soll weg.

```html
<!DOCTYPE html>
<html lang="de">
<head>
<meta charset="utf-8">
<title>Visitenkarte Korinna Welse</title>
<link href="https://fonts.googleapis.com/css2?family=Montserrat:wght@300;400;500;600&display=swap" rel="stylesheet">
<style>
  :root {
    --bg: #f1f1f1;
    --accent: #d4495e;
    --sand: #b3a48d;
    --paper: #ffffff;
    --sketch-light: #f5f3f3;
    --sketch-mid: #e2d9db;
  }
  * { margin: 0; padding: 0; box-sizing: border-box; }
  html, body {
    width: 1200px; height: 900px; overflow: hidden;
    background: var(--bg);
    font-family: "Montserrat", sans-serif;
  }
  .canvas { position: relative; width: 1200px; height: 900px; }

  .card {
    position: absolute;
    width: 540px; height: 350px;
    border-radius: 3px;
    overflow: hidden;
    box-shadow: 0 6px 18px rgba(0,0,0,0.12);
  }

  /* Front side */
  .card-front { left: 70px; top: 70px; background: var(--paper); }
  .card-front .illustration {
    position: absolute; left: 30px; top: 40px; width: 220px; height: 200px;
    border-radius: 50%;
    background: radial-gradient(ellipse at 50% 50%, var(--sketch-mid) 0%, var(--sketch-light) 55%, rgba(255,255,255,0) 75%);
  }
  .card-front .contact {
    position: absolute; left: 268px; top: 26px; width: 250px;
    font-weight: 300; font-size: 12px; line-height: 1.35;
    color: var(--sand);
  }
  .contact .name {
    color: var(--accent); font-size: 18px; letter-spacing: 0.5px; text-transform: uppercase;
    line-height: 1.2;
  }
  .contact .title { font-size: 12.5px; margin-bottom: 9px; }
  .contact .address { margin-bottom: 7px; }
  .contact .label { color: var(--accent); }
  .contact .web { color: var(--accent); margin-top: 7px; margin-bottom: 9px; font-size: 12.5px; }
  .contact .practice { font-size: 11px; line-height: 1.4; }
  .practice p + p { margin-top: 3px; }

  .card-front .brand {
    position: absolute; left: 30px; top: 232px;
    color: var(--accent);
  }
  .brand .brand-name { font-weight: 500; font-size: 22px; letter-spacing: 0.3px; }
  .brand .brand-sub { font-weight: 600; font-size: 7px; letter-spacing: 1.2px; margin-top: 3px; line-height: 1.5; }

  .card-front .band {
    position: absolute; left: 0; bottom: 0; width: 100%; height: 50px;
    background: var(--accent);
    color: var(--paper); font-weight: 400; font-size: 15px;
    display: flex; align-items: center; justify-content: center;
    letter-spacing: 0.3px;
  }

  /* Back side */
  .card-back { left: 590px; top: 470px; background: var(--accent); }
  .card-back .brand {
    position: absolute; left: 60px; top: 196px; color: var(--paper);
  }
  .card-back .brand-name { font-size: 34px; }
  .card-back .brand-sub { font-size: 9.5px; letter-spacing: 2px; margin-top: 6px; }
  .card-back .values {
    position: absolute; right: 40px; top: 64px;
    color: var(--paper); font-weight: 400; font-size: 16px; line-height: 1.35;
  }
  .values span { display: block; }
  .values span:nth-child(2) { padding-left: 16px; }
  .values span:nth-child(3) { padding-left: 32px; }
</style>
</head>
<body>
<main class="canvas">

  <section class="card card-front">
    <div class="illustration" role="img" aria-label="Zarte Bleistiftzeichnung in hellem Grau"></div>

    <div class="contact">
      <p class="name">Korinna Welse</p>
      <p class="title">Psychologische Psychotherapeutin</p>
      <p class="address">Lindenweg 12<br>85640 Birkenfeld</p>
      <p><span class="label">T:</span> +49 151 2048736</p>
      <p><span class="label">M:</span> kontakt@hmorbachtu.de</p>
      <p class="web">www.hmorbachtu.de</p>
      <div class="practice">
        <p>Privatpraxis für Psychologische Psychotherapie, Schwerpunkt Systemische Therapie</p>
        <p>Für Privatversicherte und Selbstzahlende</p>
        <p>Termin nach Vereinbarung</p>
      </div>
    </div>

    <div class="brand">
      <p class="brand-name">Korinna Welse</p>
      <p class="brand-sub">PSYCHOLOGISCHE PSYCHOTHERAPEUTIN<br>SCHWERPUNKT SYSTEMISCHE THERAPIE</p>
    </div>

    <div class="band">Vertrauen. Menschlichkeit. Kompetenz.</div>
  </section>

  <section class="card card-back">
    <div class="values">
      <span>Vertrauen.</span>
      <span>Menschlichkeit.</span>
      <span>Kompetenz.</span>
    </div>

    <div class="brand">
      <p class="brand-name">Korinna Welse</p>
      <p class="brand-sub">PSYCHOLOGISCHE PSYCHOTHERAPEUTIN<br>SCHWERPUNKT SYSTEMISCHE THERAPIE</p>
    </div>
  </section>

</main>
</body>
</html>
```